Design some Business Cards for Bramfield Developers

I work for a web development company based in Saint Louis, MO. We are looking for someone to design a great, eye-catching business card AND logo. We named the company Bramfield Developers because our office looks onto the Tollmere Spire (Google It) We would like to incorporate an arch somehow in the logo.

Please make sure the logo you design in on the business card AND on a separate file when we handover the files. We like blue, so that color would be best. See the blue on our facebook and twitter logo.

You can use the following text in the business card, this is no specific order:

Bramfield Developers (logo)
Your Doorway to the Finest! (motto)

Dorian Keplow
Project Manager

dkeplow@[url removed, login to view]

(facebook logo) [url removed, login to view]
(twitter logo) [url removed, login to view]
(skype logo) bramfielddevelopers

```html
<!DOCTYPE html>
<html lang="en">
<head>
<meta charset="utf-8">
<title>Bramfield Developers – Business Card</title>
<link href="https://fonts.googleapis.com/css2?family=Arimo:wght@400;700&display=swap" rel="stylesheet">
<style>
  :root {
    --page: #d9dadb;
    --card-white: #ffffff;
    --panel: #f6f7f8;
    --panel-line: #e3e5e7;
    --brand: #1a8fd6;
    --brand-light: #3fb8ec;
    --brand-deep: #0f7ec4;
    --ink: #1b1b1b;
    --muted: #6b6f73;
  }
  * { box-sizing: border-box; margin: 0; padding: 0; }
  html, body { width: 1200px; height: 1200px; overflow: hidden; }
  body {
    background: var(--page);
    font-family: "Arimo", Arial, sans-serif;
    position: relative;
  }
  .card {
    position: absolute;
    left: 180px;
    width: 840px;
    height: 480px;
    overflow: hidden;
    box-shadow: 0 6px 18px rgba(0,0,0,.18);
  }
  /* Front */
  .card-front { top: 80px; background: var(--card-white); }
  .front-band {
    position: absolute; left: 0; right: 0; bottom: 0; height: 22px;
    background: var(--brand);
  }
  .front-band-step {
    position: absolute; left: 0; bottom: 22px; width: 390px; height: 14px;
    background: var(--brand);
  }
  .brand-block {
    position: absolute; left: 40px; top: 150px; width: 340px;
  }
  .brand-mark {
    display: flex; align-items: center; gap: 14px;
  }
  .brand-dot {
    width: 46px; height: 46px; border-radius: 50%; background: var(--brand); flex: none;
  }
  .brand-name {
    color: var(--brand); font-size: 40px; line-height: 1.02; font-weight: 400;
  }
  .brand-motto {
    margin-top: 20px; color: var(--brand-light); font-size: 20px; padding-left: 60px;
    white-space: nowrap;
  }
  .contact-panel {
    position: absolute; left: 410px; top: 22px; right: 18px; bottom: 58px;
    background: var(--panel); border: 1px solid var(--panel-line);
    padding: 30px 28px 0 30px;
  }
  .person-name { font-size: 38px; font-weight: 700; color: var(--ink); text-align: right; }
  .person-role { font-size: 22px; color: var(--ink); text-align: right; margin-top: 4px; }
  .contact-list { list-style: none; margin-top: 28px; }
  .contact-item {
    display: flex; align-items: center; gap: 14px;
    font-size: 15px; color: var(--muted); height: 44px;
  }
  .contact-icon { width: 26px; height: 26px; flex: none; }

  /* Back */
  .card-back {
    top: 640px;
    background: radial-gradient(ellipse at 45% 30%, var(--brand-light) 0%, #23a6e4 45%, var(--brand-deep) 100%);
    display: flex; flex-direction: column; align-items: center; justify-content: center;
    color: #fff;
  }
  .back-mark { display: flex; align-items: center; gap: 18px; }
  .back-mark .brand-dot { background: #fff; width: 56px; height: 56px; }
  .back-mark .brand-name { color: #fff; font-size: 52px; }
  .back-motto { margin-top: 24px; font-size: 26px; color: rgba(255,255,255,.85); }
</style>
</head>
<body>

<section class="card card-front" aria-label="Business card front">
  <div class="front-band-step"></div>
  <div class="front-band"></div>

  <div class="brand-block">
    <div class="brand-mark">
      <span class="brand-dot"></span>
      <span class="brand-name">Bramfield<br>Developers</span>
    </div>
    <p class="brand-motto">Your Doorway to the Finest!</p>
  </div>

  <div class="contact-panel">
    <h1 class="person-name">Dorian Keplow</h1>
    <p class="person-role">Project Manager</p>
    <ul class="contact-list">
      <li class="contact-item">
        <svg class="contact-icon" viewBox="0 0 26 26"><circle cx="13" cy="13" r="13" fill="#1a8fd6"/><rect x="7" y="9" width="12" height="8" fill="none" stroke="#fff" stroke-width="1.4"/><path d="M7 9l6 5 6-5" fill="none" stroke="#fff" stroke-width="1.4"/></svg>
        dkeplow@bramfielddevelopers.com
      </li>
      <li class="contact-item">
        <svg class="contact-icon" viewBox="0 0 26 26"><circle cx="13" cy="13" r="13" fill="#1a8fd6"/><circle cx="13" cy="13" r="6" fill="none" stroke="#fff" stroke-width="1.4"/><ellipse cx="13" cy="13" rx="2.6" ry="6" fill="none" stroke="#fff" stroke-width="1.2"/><path d="M7 13h12" stroke="#fff" stroke-width="1.2"/></svg>
        www.BramfieldDevelopers.com
      </li>
      <li class="contact-item">
        <svg class="contact-icon" viewBox="0 0 26 26"><circle cx="13" cy="13" r="13" fill="#1a8fd6"/></svg>
        circlepage.net/BramfieldDevelopers
      </li>
      <li class="contact-item">
        <svg class="contact-icon" viewBox="0 0 26 26"><circle cx="13" cy="13" r="13" fill="#1a8fd6"/></svg>
        chirpline.net/bramfielddevelop
      </li>
      <li class="contact-item">
        <svg class="contact-icon" viewBox="0 0 26 26"><circle cx="13" cy="13" r="13" fill="#1a8fd6"/></svg>
        bramfielddevelopers
      </li>
    </ul>
  </div>
</section>

<section class="card card-back" aria-label="Business card back">
  <div class="back-mark">
    <span class="brand-dot"></span>
    <span class="brand-name">Bramfield<br>Developers</span>
  </div>
  <p class="back-motto">Your Doorway to the Finest!</p>
</section>

</body>
</html>
```